New singe page website for our software development company

We need a single webpage that includes information about our company, contact details and a job posting. It should scroll vertically with some cool animations and parallax scrolling effects.

We are a software development consulting company that writes custom software for our customers. The webpage should have graphics and illustrations that illustrate this.

Find our logo attached, it can be modified as needed.

Thanks for all the design. When looking through the various design it's clear to us, that car related images does not look right.

We got to have software design/engineering images instead.

Our unique selling points are:

• Custom software development
• Project Managment
• Industry Services
We want these displayed with some text and icons. The icons should either have the red/brown colour from our logo, or a colour that matches the design

Software

```html
<!DOCTYPE html>
<html lang="en">
<head>
<meta charset="utf-8">
<title>BrightCode — Custom Software Development</title>
<link rel="stylesheet" href="https://fonts.googleapis.com/css2?family=Lato:ital,wght@0,300;0,400;0,700;1,300&display=swap">
<style>
:root{
  --brand:#7a2b1c;
  --brand-dark:#582626;
  --coral:#d9585a;
  --ink:#333;
  --muted:#8a8a8a;
  --light:#f4f4f4;
  --card:#f1f1f1;
  --line:#e4e4e4;
  --team-bg:#666;
  --white:#fff;
}
*{box-sizing:border-box;margin:0;padding:0}
html,body{width:1200px;height:4346px;overflow:hidden}
body{font-family:'Lato',sans-serif;color:var(--ink);background:var(--white);position:relative}
section,header,nav,footer{position:absolute;left:0;width:1200px}
.title{position:absolute;left:0;width:100%;text-align:center;font-size:44px;font-weight:300;letter-spacing:1px;color:#444}
.title b{font-weight:400}
.rule{position:absolute;left:550px;width:100px;height:3px;background:var(--brand)}
.intro{position:absolute;left:290px;width:620px;text-align:center;font-size:14px;line-height:20px;color:var(--muted);font-weight:300}

/* hero */
.hero{top:0;height:445px;background:linear-gradient(160deg,#8d8a86 0%,#5b5855 45%,#2d2c2b 100%)}
.hero-photo{position:absolute;inset:0;background:radial-gradient(ellipse at 70% 85%,#1c1c1c 0,#3a3938 30%,rgba(0,0,0,0) 60%),linear-gradient(180deg,rgba(0,0,0,.15),rgba(0,0,0,.35))}
.hero-line{position:absolute;left:510px;width:180px;height:2px;background:var(--white)}
.hero h1{position:absolute;top:160px;width:100%;text-align:center;color:var(--white);font-weight:300;font-size:68px;letter-spacing:1px}
.hero .cta{position:absolute;left:543px;top:321px;width:114px;height:34px;border:2px solid var(--white);color:var(--white);font-size:11px;text-align:center;line-height:30px;letter-spacing:.5px}

/* nav */
.nav{top:445px;height:47px;background:var(--white);border-bottom:1px solid var(--line)}
.logo{position:absolute;left:86px;top:12px;display:flex;align-items:center;gap:6px;font-size:20px;font-weight:700;color:var(--brand)}
.logo i{width:10px;height:10px;background:var(--brand);display:block}
.menu{position:absolute;right:86px;top:16px;display:flex;gap:29px;list-style:none;font-size:12px;color:#777}
.menu li:first-child{color:var(--brand)}

/* services */
.services{top:492px;height:568px}
.cards{position:absolute;left:94px;top:298px;display:flex;gap:30px}
.svc{position:relative;width:230px;height:200px;border:1px solid var(--line);background:var(--white);text-align:center;padding-top:62px}
.svc .ico{position:absolute;left:85px;top:-42px;width:60px;height:60px;border-radius:50%;background:var(--white);display:flex;align-items:center;justify-content:center}
.svc h3{font-size:15px;font-weight:700;line-height:18px;color:#222}
.svc p{margin:10px 26px 0;font-size:12px;line-height:17px;color:#555}

/* about */
.about{top:1060px;height:538px;background:var(--light)}
.lead{position:absolute;top:170px;left:160px;width:880px;text-align:center;font-size:21px;line-height:32px;color:#888;font-weight:300}
.feat{position:absolute;width:400px;font-size:12px;line-height:17px;color:#666}
.feat h4{font-size:14px;font-weight:400;color:#333;margin-bottom:6px}
.feat.left{text-align:right;left:105px}
.feat.right{left:700px}
.round{position:absolute;width:58px;height:58px;border-radius:50%;background:var(--brand);display:flex;align-items:center;justify-content:center}

/* team */
.team{top:1598px;height:380px;background:var(--team-bg)}
.team .title{color:var(--white);font-size:26px;top:50px}
.members{position:absolute;left:102px;top:112px;display:flex;gap:28px}
.member{width:229px}
.photo{height:140px}
.member .band{height:82px;background:#555;text-align:center;padding-top:20px}
.member h3{color:var(--white);font-size:21px;font-weight:400}
.member span{font-size:12px;color:#999}

/* jobs */
.jobs{top:1978px;height:582px}
.job-list{position:absolute;left:105px;top:159px;display:flex;gap:18px}
.job{position:relative;width:237px;height:287px;background:var(--card);padding:22px 18px 0}
.date{position:absolute;left:18px;top:22px;width:36px;height:36px;border-radius:50%;background:var(--brand);color:var(--white);text-align:center;font-size:9px;line-height:10px;padding-top:8px}
.job h3{margin-left:50px;font-size:22px;font-weight:400;line-height:22px}
.job .sub{margin-left:50px;font-size:9px;color:#888}
.job .desc{margin-top:24px;font-size:9px;line-height:17px;color:#aaa;text-transform:uppercase;letter-spacing:.3px}
.job .meta{margin-top:20px;font-size:11px;color:#444;line-height:15px}
.job .meta p{padding:9px 0;border-bottom:1px solid var(--line)}
.job .meta b{font-weight:700}
.apply{position:absolute;left:40px;bottom:16px;width:157px;height:30px;background:var(--brand);color:var(--white);font-size:11px;font-weight:700;text-align:center;line-height:30px}

/* testimonials */
.clients-say{top:2560px;height:490px;background:var(--brand-dark)}
.clients-say .title{color:var(--white);font-size:34px;top:75px;letter-spacing:1px}
.clients-say .rule{background:var(--coral);top:137px}
.avatar{position:absolute;left:547px;top:191px;width:106px;height:106px;border-radius:50%;border:4px solid var(--white);background:linear-gradient(#c9c5c2,#8c8783)}
.quote{position:absolute;top:306px;width:100%;text-align:center;color:var(--white);font-size:33px;font-style:italic;font-weight:300}
.author{position:absolute;top:357px;width:100%;text-align:center;color:#c9b1b1;font-size:12px}
.dots{position:absolute;top:414px;left:582px;display:flex;gap:9px}
.dots i{width:11px;height:11px;border-radius:50%;background:#ccc;display:block}
.dots i:last-child{background:var(--coral)}

.partners{top:3050px;height:76px;background:var(--coral);display:flex;align-items:center}
.partners span{position:absolute;color:var(--white);font-size:22px;font-weight:400;transform:translateX(-50%)}

/* contact */
.contact{top:3126px;height:229px}
.map{top:3355px;height:450px;background:linear-gradient(135deg,#ecebe9,#dcdcda 50%,#e7e6e3)}
.info{top:3805px;height:53px;border-bottom:1px solid var(--line);font-size:17px;color:#555}
.info div{position:absolute;top:16px;display:flex;align-items:center;gap:10px}
.form{top:3858px;height:310px;background:var(--light)}
.field{position:absolute;left:287px;width:243px;height:40px;background:var(--white);border:1px solid var(--line);font-size:13px;color:#999;padding:11px 14px}
.message{position:absolute;left:559px;top:47px;width:354px;height:146px;background:var(--white);border:1px solid var(--line);font-size:13px;color:#999;padding:11px 14px}

.footer{top:4168px;height:178px}
.social{position:absolute;left:539px;top:55px;display:flex;gap:7px}
.social i{width:34px;height:34px;border-radius:50%;border:1px solid #bbb;display:block}
.copy{position:absolute;top:104px;width:100%;text-align:center;font-size:10px;color:#777}
</style>
</head>
<body>

<header class="hero">
  <div class="hero-photo" role="img" aria-label="Photo of a desk with a smartphone and a carbon-textured computer mouse"></div>
  <div class="hero-line" style="top:125px"></div>
  <h1>WE ARE CREATIVE</h1>
  <div class="hero-line" style="top:272px"></div>
  <div class="cta">GET STARTED</div>
</header>

<nav class="nav">
  <div class="logo"><i></i>BrightCode</div>
  <ul class="menu"><li>HOME</li><li>ABOUT</li><li>TEAM</li><li>SERVICES</li><li>WORK</li><li>PRICES</li><li>CONTACT</li><li>BLOG</li></ul>
</nav>

<section class="services">
  <h2 class="title" style="top:78px">OUR <b>SERVICES</b></h2>
  <div class="rule" style="top:141px"></div>
  <p class="intro" style="top:164px">Lorem ipsum dolor sit amet, consectetur adipisicing elit, sed do eiusmod tempor incididunt ut labore et dolore magna aliqua.</p>
  <div class="cards">
    <div class="svc">
      <div class="ico"><svg width="44" height="44" viewBox="0 0 24 24" fill="none" stroke="#7a2b1c" stroke-width="2.4" stroke-linecap="round"><path d="M4 4l16 16M20 4L9 15M4 20l4-4"/><circle cx="18" cy="6" r="2.5"/></svg></div>
      <h3>CUSTOM SOFTWARE<br>DEVELOPMENT</h3>
      <p>corper. Etiam vulputate nisi lorem, id aliquam augue tincidunt a. Sed pulvinar tortor.</p>
    </div>
    <div class="svc">
      <div class="ico"><svg width="44" height="44" viewBox="0 0 24 24" fill="#7a2b1c"><circle cx="8" cy="7" r="3.5"/><path d="M2 20c0-4 3-7 6-7s6 3 6 7z"/><rect x="16" y="12" width="2" height="8"/><rect x="19" y="9" width="2" height="11"/></svg></div>
      <h3>PROJECT<br>MANAGEMENT</h3>
      <p>corper. Etiam vulputate nisi lorem, id aliquam augue tincidunt a. Sed pulvinar tortor.</p>
    </div>
    <div class="svc">
      <div class="ico"><svg width="44" height="44" viewBox="0 0 24 24"><circle cx="12" cy="12" r="7" fill="none" stroke="#7a2b1c" stroke-width="5" stroke-dasharray="3.3 2.2"/><circle cx="12" cy="12" r="5.5" fill="#7a2b1c"/><circle cx="12" cy="12" r="2.3" fill="#fff"/></svg></div>
      <h3>INDUSTRY<br>SERVICES</h3>
      <p>corper. Etiam vulputate nisi lorem, id aliquam augue tincidunt a. Sed pulvinar tortor.</p>
    </div>
    <div class="svc">
      <div class="ico"><svg width="44" height="44" viewBox="0 0 24 24" fill="#7a2b1c"><circle cx="8" cy="8" r="3.5"/><circle cx="16" cy="8" r="3.5"/><path d="M1 20c0-4 3-7 7-7s7 3 7 7zM13 13.5c1-.4 2-.5 3-.5 4 0 7 3 7 7h-6"/></svg></div>
      <h3>OUR<br>TEAM</h3>
      <p>corper. Etiam vulputate nisi lorem, id aliquam augue tincidunt a. Sed pulvinar tortor.</p>
    </div>
  </div>
</section>

<section class="about">
  <h2 class="title" style="top:72px">ABOUT <b>US</b></h2>
  <div class="rule" style="top:135px"></div>
  <p class="lead">Duis aute irure dolor in reprehenderit in voluptate velit esse cillum dolore eu fugiat nulla pariatur. Excepteur sint occaecat cupidatat non proident.</p>
  <div class="feat left" style="top:250px"><h4>WHO ARE WE</h4>Lorem ipsum dolor sit amet, consectetur adipisicing elit, sed do eiusmod tempor incididunt ut labore et dolore magna aliqua.</div>
  <div class="round" style="left:527px;top:250px"><svg width="26" height="26" viewBox="0 0 24 24" fill="#fff"><circle cx="12" cy="8" r="4.5"/><path d="M3 22c0-5 4-8 9-8s9 3 9 8z"/></svg></div>
  <div class="round" style="left:615px;top:250px"><svg width="26" height="26" viewBox="0 0 24 24" fill="none" stroke="#fff" stroke-width="2.2"><circle cx="12" cy="12" r="9"/><circle cx="12" cy="12" r="4.5"/><circle cx="12" cy="12" r="1" fill="#fff"/></svg></div>
  <div class="feat right" style="top:250px"><h4>OUR MISSION</h4>Lorem ipsum dolor sit amet, consectetur adipisicing elit, sed do eiusmod tempor incididunt ut labore et dolore magna aliqua.</div>
  <div class="feat left" style="top:377px"><h4>WHAT WE DO</h4>Lorem ipsum dolor sit amet, consectetur adipisicing elit, sed do eiusmod tempor incididunt ut labore et dolore magna aliqua.</div>
  <div class="round" style="left:527px;top:377px"><svg width="28" height="28" viewBox="0 0 24 24" fill="none" stroke="#fff" stroke-width="2.4"><circle cx="9" cy="13" r="4.5" stroke-dasharray="2.5 1.5"/><circle cx="17" cy="7" r="3" stroke-dasharray="2 1.2"/></svg></div>
  <div class="round" style="left:615px;top:377px"><svg width="26" height="26" viewBox="0 0 24 24" fill="#fff"><path d="M12 21l-8.5-8.5A5 5 0 0112 5.5a5 5 0 018.5 7z"/></svg></div>
  <div class="feat right" style="top:377px"><h4>WE LOVE OUR CLIENTS</h4>Lorem ipsum dolor sit amet, consectetur adipisicing elit, sed do eiusmod tempor incididunt ut labore et dolore magna aliqua.</div>
</section>

<section class="team">
  <h2 class="title">OUR <b>TEAM</b></h2>
  <div class="members">
    <div class="member"><div class="photo" role="img" aria-label="Portrait photo of a team member" style="background:linear-gradient(135deg,#6c7b8a,#2f3841)"></div><div class="band"><h3>JOHN DOE</h3><span>Lorem Ipsum</span></div></div>
    <div class="member"><div class="photo" role="img" aria-label="Portrait photo of a team member" style="background:linear-gradient(135deg,#5b3a36,#a27362)"></div><div class="band"><h3>JOHN DOE</h3><span>Lorem Ipsum</span></div></div>
    <div class="member"><div class="photo" role="img" aria-label="Portrait photo of a team member" style="background:linear-gradient(135deg,#d8dad5,#7e8a86)"></div><div class="band"><h3>JOHN DOE</h3><span>Lorem Ipsum</span></div></div>
    <div class="member"><div class="photo" role="img" aria-label="Portrait photo of a team member" style="background:linear-gradient(135deg,#4a3a48,#a2574a)"></div><div class="band"><h3>JOHN DOE</h3><span>Lorem Ipsum</span></div></div>
  </div>
</section>

<section class="jobs">
  <h2 class="title" style="top:50px">JOB <b>LISTING</b></h2>
  <div class="rule" style="top:112px"></div>
  <div class="job-list">
    <div class="job"><div class="date">27<br>MAR</div><h3>TESTING</h3><p class="sub">LOREM IPSUM</p><p class="desc">Lorem ipsum dolor sit amet, con sectetur adipiscing elit. Proin nibh augue, suscipit a, scelerisque sed, lacinia in, mi. Cras vel lorem. Etiam pellentesque aliquet.</p><div class="meta"><p><b>JOB ROLE :</b> TECHNOLOGY / IT</p><p><b>CARRER LEVEL :</b> MID CAREER</p></div><div class="apply">APPLY FOR THIS JOB</div></div>
    <div class="job"><div class="date">27<br>MAR</div><h3>TESTING</h3><p class="sub">LOREM IPSUM</p><p class="desc">Lorem ipsum dolor sit amet, con sectetur adipiscing elit. Proin nibh augue, suscipit a, scelerisque sed, lacinia in, mi. Cras vel lorem. Etiam pellentesque aliquet.</p><div class="meta"><p><b>JOB ROLE :</b> TECHNOLOGY / IT</p><p><b>CARRER LEVEL :</b> MID CAREER</p></div><div class="apply">APPLY FOR THIS JOB</div></div>
    <div class="job"><div class="date">27<br>MAR</div><h3>TESTING</h3><p class="sub">LOREM IPSUM</p><p class="desc">Lorem ipsum dolor sit amet, con sectetur adipiscing elit. Proin nibh augue, suscipit a, scelerisque sed, lacinia in, mi. Cras vel lorem. Etiam pellentesque aliquet.</p><div class="meta"><p><b>JOB ROLE :</b> TECHNOLOGY / IT</p><p><b>CARRER LEVEL :</b> MID CAREER</p></div><div class="apply">APPLY FOR THIS JOB</div></div>
    <div class="job"><div class="date">27<br>MAR</div><h3>TESTING</h3><p class="sub">LOREM IPSUM</p><p class="desc">Lorem ipsum dolor sit amet, con sectetur adipiscing elit. Proin nibh augue, suscipit a, scelerisque sed, lacinia in, mi. Cras vel lorem. Etiam pellentesque aliquet.</p><div class="meta"><p><b>JOB ROLE :</b> TECHNOLOGY / IT</p><p><b>CARRER LEVEL :</b> MID CAREER</p></div><div class="apply">APPLY FOR THIS JOB</div></div>
  </div>
</section>

<section class="clients-say">
  <h2 class="title">WHAT OUR CLIENTS SAY</h2>
  <div class="rule"></div>
  <div class="avatar" role="img" aria-label="Portrait photo of the client"></div>
  <p class="quote">"I love this template! Congratulations!"</p>
  <p class="author">Marta - Harbor Group</p>
  <div class="dots"><i></i><i></i><i></i></div>
</section>

<section class="partners">
  <span style="left:220px">Orbit Design</span>
  <span style="left:483px">Harbor Group</span>
  <span style="left:726px">Pixel Works</span>
  <span style="left:980px">Nimbus Inc.</span>
</section>

<section class="contact">
  <h2 class="title" style="top:75px">CONTACT <b>US</b></h2>
  <div class="rule" style="top:138px"></div>
  <p class="intro" style="top:162px">Lorem ipsum dolor sit amet, consectetur adipisicing elit, sed do eiusmod tempor incididunt ut labore et dolore magna aliqua.</p>
</section>

<section class="map" role="img" aria-label="Street map of the city with a location pin at the office"></section>

<section class="info">
  <div style="left:200px"><svg width="14" height="18" viewBox="0 0 14 18"><path d="M7 0a7 7 0 00-7 7c0 5 7 11 7 11s7-6 7-11a7 7 0 00-7-7z" fill="#777"/><circle cx="7" cy="7" r="2.5" fill="#fff"/></svg>Lakeview, UK</div>
  <div style="left:503px"><svg width="16" height="16" viewBox="0 0 24 24" fill="#777"><path d="M6 2l4 5-2.5 2.5a13 13 0 007 7L17 14l5 4-2.5 3.5C11 21 3 13 2.5 4.5z"/></svg>+44 (0)1-234-5678</div>
  <div style="left:843px"><svg width="18" height="14" viewBox="0 0 18 14"><rect width="18" height="14" rx="1" fill="#777"/><path d="M1 1l8 6 8-6" fill="none" stroke="#fff" stroke-width="1.5"/></svg>hello@brightcode.dev</div>
</section>

<section class="form">
  <div class="field" style="top:47px">Full Name</div>
  <div class="field" style="top:100px">Email</div>
  <div class="field" style="top:154px">Phone</div>
  <div class="message">Message</div>
</section>

<footer class="footer">
  <div class="social"><i></i><i></i><i></i></div>
  <p class="copy">2016 © BRIGHTCODE. All rights reserved</p>
</footer>

</body>
</html>
```